Brent Oakes Director / Photographer Branding

I need note pads, envelops, business cards and letter head for my company. I'm a fashion and advertising director / photographer. I'm having trouble deciding how to include both Director & Photographer in my title or if it is even necessary. Maybe just my name is enough. I'm open for even using my initials if it works with the design and overall pieces. Please view my website to see what I have at this moment and what work I do. www.brentoakesstudio-mail.net
Updates

Project Deadline Extended
Reason: Hello Everyone! I'm extending the deadline since I have been traveling on a job out of country and I wanted to have more time to look through all the designs and give enough time for everyone to provide changes with designs and updates. I will be more available to communicate online now that I'm back in the office! Thank you! Brent Oakes

Target Market(s)

Fashion magazines, clothing lines and beauty cosmetic brands.

Industry/Entity Type

Fashion Photography

Font styles to use
Sans Serif

Colors
acd036
acd35d
cbcbcb
f5f5f5

Requirements
Must have
• My name.. Brent Oakes, my website: brentoakesstudio-mail.net my phone number, 555-284-6103
• I don't need my address on these. I also live by the philosophy that less is more and keeping things simple ads strength to a design. I also don't want to stop people from taking chances and experimenting with an idea that might take me down different road with my branding.
Nice to have
• Bold designs and clean lines. I'm open to ideas that I could adopt but I lean towards a more minimalistic look in general.
Should not have
• Not have cheesy graphics or pictures. No images of cameras, film or anything that looks like it is a camera or aperture, lens etc... ;)

```html
<!DOCTYPE html>
<html lang="en">
<head>
<meta charset="utf-8">
<title>Brent Oakes — Business Cards</title>
<link rel="stylesheet" href="https://fonts.googleapis.com/css2?family=Jost:wght@300;400&display=swap">
<style>
  :root {
    --lime: #9bc324;
    --paper: #f5f5f5;
    --ink: #1a1a1a;
    --backdrop: #2b2b2b;
    --white: #ffffff;
  }
  html, body {
    margin: 0;
    padding: 0;
    width: 1200px;
    height: 900px;
    overflow: hidden;
    background: var(--backdrop);
    font-family: "Jost", sans-serif;
  }
  .stage {
    position: relative;
    width: 1200px;
    height: 900px;
  }
  .card {
    position: absolute;
    top: 188px;
    width: 300px;
    height: 525px;
    box-sizing: border-box;
  }
  .card--front {
    left: 250px;
    background: var(--lime);
    color: var(--white);
  }
  .card--back {
    left: 650px;
    background: var(--paper);
    color: var(--ink);
  }
  .card__title-vertical {
    position: absolute;
    top: 22px;
    left: 14px;
    writing-mode: vertical-rl;
    font-size: 12px;
    font-weight: 400;
    letter-spacing: 0.02em;
  }
  .card__name {
    position: absolute;
    margin: 0;
    writing-mode: vertical-rl;
    font-weight: 300;
    font-size: 46px;
    line-height: 0.95;
    letter-spacing: 0.02em;
    text-transform: uppercase;
  }
  .card--front .card__name {
    right: 20px;
    bottom: 20px;
  }
  .card--back .card__name {
    top: 22px;
    left: 22px;
    height: 200px;
    text-align: end;
    transform: rotate(180deg);
  }
  .card__details {
    position: absolute;
    left: 24px;
    bottom: 26px;
    font-size: 14px;
    font-weight: 400;
    line-height: 1.3;
  }
  .card__role {
    margin: 0 0 14px;
  }
  .card__contact {
    margin: 0;
  }
</style>
</head>
<body>
  <main class="stage">
    <section class="card card--front">
      <span class="card__title-vertical">Director &amp; Photographer</span>
      <h1 class="card__name">Brent<br>Oakes</h1>
    </section>
    <section class="card card--back">
      <h2 class="card__name">Brent<br>Oakes</h2>
      <div class="card__details">
        <p class="card__role">Director &amp; Photographer</p>
        <p class="card__contact">brentoakesstudio-mail.net<br>555-284-6103</p>
      </div>
    </section>
  </main>
</body>
</html>
```